Flyer-Design für Hersteller von ökologischen Werbemitteln aus Papier/Karton
Zielgruppe
Wir machen ökologische Werbemittel aus Papier/Karton wie Parkscheiben, Drehscheiben usw.
Aufgabenstellung
Wir suchen den Content für einen Falzflyer im Format 220 x 150 mm (offen) bzw. 110 x 150 mm (geschlossen) mit folgenden Inhalten.
Seite 1: Frei/Leer
Seite 2 (Innen) : Speisekarte Pizzeria Valtoro Teil I (einfach ein paar Pizzen)
Seite 3 (Innen): Speiseikarte Pizzeria Valtoro Teil II (einfach ein paar Nudelgerichte)
Seite 4 (Rückseite): Zehn leere Felder für Stempel Pizzeria Valtoro (nach zehn Stempeln bekommt der Käufer eine Pizza gratis)
Das gesamte Design/Layout in einem Pizzierastyle.

```html
<!DOCTYPE html>
<html lang="de">
<head>
<meta charset="utf-8">
<title>Pizzeria Valtoro – Speisekarte &amp; Bonus-Pass</title>
<link href="https://fonts.googleapis.com/css2?family=Yellowtail&family=Archivo+Narrow:wght@400;500&display=swap" rel="stylesheet">
<style>
  :root {
    --page-bg: #ffffff;
    --board: #141414;
    --board-light: #2a2a2a;
    --chalk: #f2f2f2;
    --chalk-soft: #d9d9d9;
    --accent: #c4501f;
    --field: #3a3a3a;
    --crust: #c9894a;
    --sauce: #a8321c;
  }
  * { margin: 0; padding: 0; box-sizing: border-box; }
  html, body { width: 1200px; height: 3128px; overflow: hidden; background: var(--page-bg); }
  body { position: relative; font-family: "Archivo Narrow", "Arial Narrow", sans-serif; color: var(--chalk); }

  .chalkboard {
    position: absolute;
    background: radial-gradient(ellipse at 40% 35%, var(--board-light) 0%, var(--board) 60%, #0b0b0b 100%);
    overflow: hidden;
  }

  /* Menu spread */
  .menu-spread { left: 44px; top: 1165px; width: 1104px; height: 755px; }
  .menu-title {
    position: absolute; left: 50px; top: 20px; width: 480px; height: 180px;
    display: flex; justify-content: center; align-items: flex-end; gap: 16px;
    font-family: "Yellowtail", cursive; font-weight: 400; font-size: 92px; color: #fff;
    line-height: 1; white-space: nowrap;
  }
  .menu-title .word { display: block; padding-bottom: 6px; }
  .menu-title .amp { display: block; font-size: 170px; color: var(--accent); line-height: 0.95; }

  .menu-column { position: absolute; width: 496px; }
  .menu-column.pizzas { left: 30px; top: 232px; }
  .menu-column.pastas { left: 578px; top: 22px; width: 498px; }
  .dish { height: 68px; }
  .dish-line { display: flex; align-items: baseline; font-family: "Yellowtail", cursive; font-size: 25px; line-height: 30px; white-space: nowrap; }
  .dish-leader { flex: 1; border-bottom: 2px dotted var(--chalk-soft); margin: 0 3px; transform: translateY(-6px); }
  .dish-desc { font-size: 15px; line-height: 18px; color: var(--chalk); white-space: nowrap; }

  .footnote {
    position: absolute; left: 578px; top: 593px; width: 290px;
    font-size: 14px; line-height: 19px; color: var(--chalk-soft);
  }
  .pizza-photo {
    position: absolute; left: 830px; top: 534px; width: 420px; height: 420px; border-radius: 50%;
    background: radial-gradient(circle at 45% 40%, #e8d3b0 0%, var(--sauce) 35%, #d4a070 62%, var(--crust) 75%, #8a5a2c 100%);
  }

  /* Bonus card */
  .bonus-card { left: 321px; top: 2072px; width: 556px; height: 758px; }
  .bonus-title {
    position: absolute; top: 16px; width: 100%; text-align: center;
    font-family: "Yellowtail", cursive; font-weight: 400; font-size: 58px; color: #fff; line-height: 1.1;
  }
  .bonus-intro { position: absolute; left: 42px; top: 98px; width: 490px; font-size: 15px; line-height: 19px; color: var(--chalk-soft); }
  .stamp-grid {
    position: absolute; left: 41px; top: 143px;
    display: grid; grid-template-columns: 225px 225px; column-gap: 34px; row-gap: 33px;
  }
  .stamp-field {
    height: 70px; border: 2px solid var(--accent); background: var(--field);
    display: flex; align-items: center; justify-content: center;
    font-family: "Yellowtail", cursive; font-size: 56px; line-height: 1; color: #fff;
  }
  .bonus-logo {
    position: absolute; left: 41px; top: 652px; width: 76px; height: 76px; border-radius: 50%;
    background: #fff; color: #333; display: flex; align-items: center; justify-content: center; font-size: 16px;
  }
  .bonus-phone {
    position: absolute; left: 132px; right: 24px; top: 650px; text-align: center;
    font-family: "Yellowtail", cursive; font-size: 50px; color: var(--accent);
    line-height: 1; white-space: nowrap;
  }
  .bonus-address {
    position: absolute; left: 132px; right: 24px; top: 724px; text-align: center;
    font-size: 15px; line-height: 18px; color: var(--chalk-soft); white-space: nowrap;
  }
</style>
</head>
<body>

<section class="chalkboard menu-spread">
  <h1 class="menu-title"><span class="word">Pizza</span><span class="amp">&amp;</span><span class="word">Pasta</span></h1>

  <div class="menu-column pizzas">
    <div class="dish"><div class="dish-line"><span>Margerita</span><span class="dish-leader"></span><span>€ 5,20</span></div><div class="dish-desc">Tomaten, Käse, Oregano</div></div>
    <div class="dish"><div class="dish-line"><span>Romana</span><span class="dish-leader"></span><span>€5,90</span></div><div class="dish-desc">Tomaten, Käse, Sardinen</div></div>
    <div class="dish"><div class="dish-line"><span>Gemüsepizza</span><span class="dish-leader"></span><span>€ 5,90</span></div><div class="dish-desc">Mais, Zwiebel, Champignons, Spargel und Käse</div></div>
    <div class="dish"><div class="dish-line"><span>Spinaci</span><span class="dish-leader"></span><span>€ 6, 20</span></div><div class="dish-desc">Tomaten, Käse, Spinat</div></div>
    <div class="dish"><div class="dish-line"><span>Salami</span><span class="dish-leader"></span><span>€ 6,50</span></div><div class="dish-desc">Tomaten, Käse, Salami</div></div>
    <div class="dish"><div class="dish-line"><span>Al Tonno</span><span class="dish-leader"></span><span>€ 6,30</span></div><div class="dish-desc">Tomaten, Käse, Thunfisch</div></div>
    <div class="dish"><div class="dish-line"><span>Spaghetti Napoli</span><span class="dish-leader"></span><span>€ 6,50</span></div><div class="dish-desc">mit Tomaten und Knoblauch</div></div>
  </div>

  <div class="menu-column pastas">
    <div class="dish"><div class="dish-line"><span>Spaghetti Bolognese</span><span class="dish-leader"></span><span>€ 6,70</span></div><div class="dish-desc">mit Fleischsauce</div></div>
    <div class="dish"><div class="dish-line"><span>Spaghetti Aglio</span><span class="dish-leader"></span><span>€ 6,50</span></div><div class="dish-desc">mit Knoblauch, Öl, Pfefferoni</div></div>
    <div class="dish"><div class="dish-line"><span>Spaghetti Diavolo</span><span class="dish-leader"></span><span>€ 6,50</span></div><div class="dish-desc">mit Tomaten, Schinken, Pfefferoni</div></div>
    <div class="dish"><div class="dish-line"><span>Spaghetti ala Carbonara</span><span class="dish-leader"></span><span>€ 6,50</span></div><div class="dish-desc">mit Speck, Ei, Schlagobers</div></div>
    <div class="dish"><div class="dish-line"><span>Spaghetti Della Casa</span><span class="dish-leader"></span><span>€ 6,50</span></div><div class="dish-desc">mit Tomaten, Paprika, Schafskäse</div></div>
    <div class="dish"><div class="dish-line"><span>Gnocchi al Ragù</span><span class="dish-leader"></span><span>€ 6,50</span></div><div class="dish-desc">mit Fleischsauce</div></div>
    <div class="dish"><div class="dish-line"><span>Gnocchi Diavolo</span><span class="dish-leader"></span><span>€ 7,00</span></div><div class="dish-desc">Kartoffelnockern mit Tomaten, Schinken, Pfefferoni</div></div>
    <div class="dish"><div class="dish-line"><span>Gnocchi Alla Chef</span><span class="dish-leader"></span><span>€ 7,00</span></div><div class="dish-desc">mit Gorgonzolakäse und Schinken</div></div>
  </div>

  <p class="footnote">* Lest, officiae ea derum lab ipis quam aborecum nonsed quas ande sandi autem. Inc­tiistibus del im as audic tes mosapidis ipsande llabo. Itaernam, invelest, con periand itiunt</p>

  <div class="pizza-photo" role="img" aria-label="Foto einer Pizza mit Tomaten, Mozzarella, Oliven und Basilikum auf einem Holzbrett"></div>
</section>

<section class="chalkboard bonus-card">
  <h2 class="bonus-title">Bonus-Pass</h2>
  <p class="bonus-intro">Für jede Pizza oder Pasta erhalten Sie einen Stempel. Wenn diese Bonuskarte voll ist, erhalten Sie eine Pizza oder Pasta gratis!</p>
  <div class="stamp-grid">
    <div class="stamp-field">1</div><div class="stamp-field">2</div>
    <div class="stamp-field">3</div><div class="stamp-field">4</div>
    <div class="stamp-field">5</div><div class="stamp-field">6</div>
    <div class="stamp-field">7</div><div class="stamp-field">8</div>
    <div class="stamp-field">9</div><div class="stamp-field">10</div>
  </div>
  <div class="bonus-logo">LOGO</div>
  <div class="bonus-phone">Tel. 04793 58 107</div>
  <p class="bonus-address">Pizzeria Valtoro | Lindenweg 42 | 47611 Bergenfeld</p>
</section>

</body>
</html>
```